Business card for wedding & event planning company

I'm looking for a well designed double sided business card to represent my wedding and event planning company.

It should include the fact we manage the following events:
Weddings, birthdays, conferences, product launches, fashion shows & conventions
in the following areas:
Wiltshire, Oxfordshire, Berkshire & London

My contact details to be included are:

Moira Lintell
07741 308562
moira@amberfinchgatherings.co.uk
www.amberfinchgatherings.co.uk

My logo can be found at the following Filevaultly location:
AI file: https://www.filevaultly.com/s/k3mprt8wq51bn2x/brief_480317_2290451_7735102_sourcefile.ai?dl=0
PNG file:
https://www.filevaultly.com/s/hv7ncqeyb4tlofu/brief_480317_2290451_7735102_e8a1b406_image.png?dl=0

Target Market(s)

women aged 30-55

Industry/Entity Type

Wedding

Contact Information for Business Card

in the following areas:

Moira Lintell
Event Planner
07741 308562

Font styles to use
Serif
Sans Serif
Script

Requirements
Must have
• Purple and white colour scheme
Should not have
• Black background
• Please don't submit any of the see-through business card designs.

```html
<!DOCTYPE html>
<html lang="en">
<head>
<meta charset="utf-8">
<title>Amber Finch Gatherings – Business Card</title>
<link rel="stylesheet" href="https://fonts.googleapis.com/css2?family=Crimson+Pro:wght@400;600;700&display=swap">
<style>
  :root {
    --backdrop: #f2f0ec;
    --card-white: #ffffff;
    --plum: #8a2a96;
    --plum-deep: #7a2087;
    --plum-soft: #b58abd;
    --lilac-line: #cdb6d2;
    --text-on-plum: #ffffff;
    --text-on-plum-soft: rgba(255, 255, 255, 0.88);
  }
  html, body {
    margin: 0;
    padding: 0;
    width: 1200px;
    height: 1000px;
    overflow: hidden;
    background: var(--backdrop);
  }
  .canvas {
    position: relative;
    width: 1200px;
    height: 1000px;
    font-family: "Crimson Pro", Georgia, serif;
  }
  .card {
    position: absolute;
    top: 205px;
    width: 380px;
    height: 590px;
    box-shadow: 0 12px 30px rgba(0, 0, 0, 0.16);
    overflow: hidden;
  }
  .card--front {
    left: 170px;
    background: var(--card-white);
  }
  .card--back {
    left: 650px;
    background: linear-gradient(180deg, var(--plum) 0%, #a763b0 30%, #d9c0dd 55%, var(--card-white) 72%);
  }

  /* Front: brand lockup */
  .brand {
    position: absolute;
    left: 0;
    right: 0;
    top: 230px;
    text-align: center;
  }
  .brand__mark {
    display: block;
    margin: 0 auto 18px;
  }
  .brand__name {
    margin: 0;
    color: var(--plum);
    font-weight: 400;
    font-size: 34px;
    letter-spacing: 1px;
    line-height: 1.1;
  }
  .brand__rule {
    width: 260px;
    height: 1px;
    margin: 14px auto 0;
    background: var(--lilac-line);
  }

  /* Back */
  .back__ring {
    position: absolute;
    left: -60px;
    top: 110px;
  }
  .back__content {
    position: absolute;
    right: 30px;
    top: 36px;
    text-align: right;
  }
  .areas {
    margin: 0;
    color: var(--text-on-plum);
    font-weight: 700;
    font-size: 21px;
    line-height: 1.1;
  }
  .services {
    list-style: none;
    margin: 14px 0 0;
    padding: 0;
    color: var(--text-on-plum-soft);
    font-size: 17px;
    line-height: 1.45;
  }
  .contact {
    position: absolute;
    right: 30px;
    bottom: 38px;
    text-align: right;
    color: var(--plum-deep);
    line-height: 1.25;
  }
  .contact__name {
    margin: 0 0 2px;
    font-weight: 700;
    font-size: 22px;
  }
  .contact__line {
    margin: 0;
    font-size: 17px;
  }
  .contact__email {
    margin-top: 22px;
  }
  .contact__web {
    font-weight: 700;
    font-size: 18px;
  }
</style>
</head>
<body>
<main class="canvas">
  <section class="card card--front" aria-label="Business card front">
    <div class="brand">
      <svg class="brand__mark" width="64" height="64" viewBox="0 0 64 64" aria-hidden="true">
        <circle cx="32" cy="32" r="29" fill="none" stroke="var(--plum)" stroke-width="2"/>
      </svg>
      <p class="brand__name">Amber Finch Gatherings</p>
      <div class="brand__rule"></div>
    </div>
  </section>

  <section class="card card--back" aria-label="Business card back">
    <svg class="back__ring" width="340" height="340" viewBox="0 0 340 340" aria-hidden="true">
      <circle cx="170" cy="170" r="160" fill="none" stroke="rgba(255,255,255,0.85)" stroke-width="2.5"/>
    </svg>
    <div class="back__content">
      <p class="areas">Wiltshire, Oxfordshire,<br>Berkshire &amp; London</p>
      <ul class="services">
        <li>Weddings</li>
        <li>Birthdays</li>
        <li>Conferences</li>
        <li>Product launches</li>
        <li>Fashion shows</li>
        <li>Conventions</li>
      </ul>
    </div>
    <div class="contact">
      <p class="contact__name">Moira Lintell</p>
      <p class="contact__line">07741 308562</p>
      <p class="contact__line contact__email">moira@amberfinchgatherings.co.uk</p>
      <p class="contact__line contact__web">www.amberfinchgatherings.co.uk</p>
    </div>
  </section>
</main>
</body>
</html>
```